Luxury Jewelry & Watch Company Website Design

At Vexaro, we are a brand that designs and sells unique Jewelry & Watches for Men and Women. We are looking to transform our current e-commerce website, which looks like a boring catalog, into a more EXCLUSIVE, luxurious, and unique website experience... CLASSY, yet MODERN...We want customers/ clients to be drawn into our brand and our products.. essentially to turn them into buying customers. We want them to feel the exclusiveness of our brand and how different we are from the rest of the industry. The website has to convey the feel and culture of our brand, but stay simple to navigate.

We sell direct to the consumer online as well as wholesale to retailers, And now we are opening our first store in March..So the website should appeal to all areas. Id like to have a place on the website for our upcoming store, it would be sweet to have an area where clients can setup an appointment to meet with me at the store to go over and Jewelry, watches, or Custom Jewelry Design. In March, we will have professional photos of the store as well as professional photos of models wearing the Jewelry & Watches. So please make space for all of those new photos to be implemented.

That should be it! It all comes down to creating a Luxurious, Exclusive, and Unique website that portrays Vexaro and brings in clientele and seals the deal for sales!

Thank you very much! We are extremely excited to see all your awesome designs!

Target Market(s)

25-40 year old successful Men & Women... The young professionals crowd.

Industry/Entity Type

E-Commerce

Requirements
Must have
• Luxury, Exclusive feeling (like Corvane, Marrow Peak Vodka, ext), Simplicity, Brand Culture, Watches are our main product, Appeal to both Men & Women. Also, an elegant banner for promotions, that i am able to update myself.
Nice to have
• Store Appointment Scheduler, updated area that shows which celebs/ stars are wearing the goods, History of the brand and products

```html
<!DOCTYPE html>
<html lang="en">
<head>
<meta charset="utf-8">
<title>Vexaro – Jewellery &amp; Watches</title>
<link href="https://fonts.googleapis.com/css2?family=Didact+Gothic&family=Open+Sans:wght@600;700&display=swap" rel="stylesheet">
<style>
  :root {
    --charcoal: #383d42;
    --page: #f1f1f1;
    --white: #ffffff;
    --ink: #111111;
    --text: #555555;
    --rule: #cfcfcf;
    --frame: #d9d9d9;
    --slate-dark: #5a646c;
    --slate-light: #8e989f;
    --button: #6d767d;
    --dot: #9a9a9a;
    --dot-active: #c58a5c;
    --social: #7b848b;
  }
  * { margin: 0; padding: 0; box-sizing: border-box; }
  html, body { width: 1200px; height: 950px; overflow: hidden; }
  body {
    position: relative;
    background: radial-gradient(ellipse at 50% 40%, #ffffff 0%, #f6f6f6 55%, #ebebeb 100%);
    font-family: Arial, Helvetica, sans-serif;
    color: var(--ink);
  }
  .top-bar { position: absolute; left: 0; top: 0; width: 1200px; height: 17px; background: var(--charcoal); }

  .brand {
    position: absolute; left: 120px; top: 36px;
    font-family: "Didact Gothic", sans-serif; font-size: 52px; line-height: 60px;
    color: var(--ink); letter-spacing: 1px;
  }

  .main-nav { position: absolute; left: 488px; top: 62px; width: 586px; height: 37px; }
  .main-nav ul { list-style: none; display: flex; justify-content: space-between; padding: 0 0 0 3px; }
  .main-nav a {
    font-family: "Didact Gothic", sans-serif; font-size: 15px; color: var(--ink);
    text-decoration: none; letter-spacing: 0.3px;
  }
  .nav-track { position: absolute; left: 0; top: 32px; width: 586px; height: 4px; background: var(--rule); }
  .nav-active { position: absolute; left: 0; top: 32px; width: 48px; height: 4px; background: var(--charcoal); }
  .nav-pointer { position: absolute; left: 18px; top: 27px; }

  .hero-shadow {
    position: absolute; left: 160px; top: 488px; width: 920px; height: 40px;
    background: radial-gradient(ellipse at 50% 0%, rgba(0,0,0,0.18) 0%, rgba(0,0,0,0) 70%);
  }
  .hero-frame {
    position: absolute; left: 120px; top: 122px; width: 961px; height: 371px;
    background: var(--white); border: 1px solid var(--frame);
    box-shadow: 0 1px 2px rgba(0,0,0,0.08);
  }
  .hero-image {
    position: absolute; left: 10px; top: 9px; width: 940px; height: 350px;
    background: radial-gradient(ellipse at 45% 20%, #b9c4ca 0%, #8c969d 45%, #4d545b 100%);
  }
  .hero-arrow {
    position: absolute; top: 152px; width: 22px; height: 36px;
    background: rgba(255,255,255,0.25);
  }
  .hero-arrow.prev { left: 0; border-radius: 0 4px 4px 0; }
  .hero-arrow.next { right: 0; border-radius: 4px 0 0 4px; }
  .hero-arrow svg { position: absolute; left: 7px; top: 12px; }
  .hero-dots {
    position: absolute; left: 407px; top: 322px; width: 126px; height: 28px;
    background: #e2e2e2; border-radius: 5px 5px 0 0;
    display: flex; justify-content: center; align-items: center; gap: 7px;
  }
  .hero-dots span { width: 12px; height: 12px; border-radius: 50%; background: var(--dot); box-shadow: inset 0 1px 1px rgba(0,0,0,0.3); }
  .hero-dots span.active { background: var(--dot-active); }

  .tile {
    position: absolute; top: 548px; width: 300px; height: 184px;
    border: 1px solid #dcdcdc; background: var(--white);
  }
  .history { left: 120px; }
  .history h2 {
    font-family: "Didact Gothic", sans-serif; font-weight: 400; font-size: 24px;
    color: #333; padding: 14px 0 0 10px; height: 55px;
  }
  .history .divider { height: 1px; background: #dcdcdc; }
  .history p {
    padding: 9px 8px 0 8px; font-size: 12px; line-height: 15.2px; color: var(--text); text-align: justify;
  }
  .portrait {
    left: 450px;
    background: linear-gradient(160deg, #d8d8d8 0%, #9a9a9a 45%, #3a3a3a 70%, #7d7d7d 100%);
  }
  .promo {
    left: 780px; overflow: hidden;
    background: linear-gradient(180deg, #c4ccd1 0%, #e4e7e9 50%, #b9c1c6 100%);
    text-align: center;
  }
  .promo .promo-brand {
    font-family: "Didact Gothic", sans-serif; font-size: 46px; color: var(--ink);
    padding-top: 20px; line-height: 56px;
  }
  .promo .promo-line {
    font-family: "Open Sans", sans-serif; font-weight: 700; font-size: 27px; line-height: 34px;
    color: var(--ink); margin-top: 22px;
  }

  .appointment {
    position: absolute; left: 120px; top: 773px; width: 960px; height: 82px;
    background: linear-gradient(180deg, var(--slate-dark) 0%, var(--slate-light) 100%);
    color: var(--white); font-family: "Open Sans", sans-serif;
  }
  .appointment .clock { position: absolute; left: 26px; top: 6px; }
  .appointment h2 {
    position: absolute; left: 149px; top: 16px; font-weight: 600; font-size: 36px; line-height: 44px;
  }
  .appointment .hours { position: absolute; left: 516px; top: 27px; font-weight: 600; font-size: 18px; line-height: 24px; }
  .appointment .book {
    position: absolute; left: 668px; top: 20px; width: 282px; height: 43px;
    background: var(--button); color: var(--white); text-decoration: none;
    font-weight: 600; font-size: 17px; letter-spacing: 0.3px;
    display: flex; align-items: center; justify-content: center;
  }

  .site-footer { position: absolute; left: 0; top: 881px; width: 1200px; height: 69px; background: var(--charcoal); }
  .site-footer small { position: absolute; left: 120px; top: 22px; font-size: 12px; color: #e8e8e8; }
  .social { position: absolute; left: 968px; top: 13px; display: flex; gap: 8px; }
  .social a { width: 32px; height: 32px; border-radius: 50%; background: var(--social); display: block; }
</style>
</head>
<body>
  <div class="top-bar"></div>

  <header>
    <div class="brand">Vexaro</div>
    <nav class="main-nav">
      <ul>
        <li><a href="#">HOME</a></li>
        <li><a href="#">ABOUT</a></li>
        <li><a href="#">JEWELLERY</a></li>
        <li><a href="#">WATCHES</a></li>
        <li><a href="#">SERVICES</a></li>
        <li><a href="#">CONTACT</a></li>
      </ul>
      <div class="nav-track"></div>
      <div class="nav-active"></div>
      <svg class="nav-pointer" width="10" height="5" viewBox="0 0 10 5"><path d="M0 5 L5 0 L10 5 Z" fill="#383d42"/></svg>
    </nav>
  </header>

  <div class="hero-shadow"></div>
  <section class="hero-frame">
    <div class="hero-image" role="img" aria-label="Row of six silver diamond-set rings reflected on a grey surface">
      <div class="hero-arrow prev"><svg width="8" height="12" viewBox="0 0 8 12"><path d="M7 1 L2 6 L7 11" stroke="#fff" stroke-width="2" fill="none"/></svg></div>
      <div class="hero-arrow next"><svg width="8" height="12" viewBox="0 0 8 12"><path d="M1 1 L6 6 L1 11" stroke="#fff" stroke-width="2" fill="none"/></svg></div>
      <div class="hero-dots"><span></span><span></span><span class="active"></span><span></span><span></span></div>
    </div>
  </section>

  <main>
    <article class="tile history">
      <h2>Our History</h2>
      <div class="divider"></div>
      <p>Sed ut perspiciatis unde omnis iste natus error sit voluptatem accusantium doloremque laudantium, totam rem aperiam, eaque ipsa quae ab illo inventore veritatis et quasi architecto beatae vitae dicta sunt explicabo. oluptas sit aspernatur aut odit aut fugit, sed quia consequuntur magni dolores eos qui ratione voluptatem sequi nesciunt.</p>
    </article>

    <div class="tile portrait" role="img" aria-label="Black and white photo of a man in a suit stepping out of a luxury car"></div>

    <div class="tile promo" role="img" aria-label="Silver rings in the background behind the brand promotion">
      <div class="promo-brand">Vexaro</div>
      <div class="promo-line">Jewellery &amp; watches<br>for Men &amp; Women</div>
    </div>

    <section class="appointment">
      <svg class="clock" width="72" height="70" viewBox="0 0 72 70" aria-hidden="true">
        <circle cx="34" cy="33" r="31" fill="#f2a21c"/>
        <circle cx="34" cy="33" r="25" fill="#ffffff"/>
        <path d="M34 14 V33 L46 40" stroke="#333" stroke-width="2.5" fill="none" stroke-linecap="round"/>
        <circle cx="34" cy="33" r="2.5" fill="#333"/>
        <rect x="44" y="40" width="26" height="26" rx="5" fill="#e8562a"/>
        <rect x="49" y="47" width="16" height="14" rx="2" fill="#ffd37a"/>
      </svg>
      <h2>Store Appointment</h2>
      <div class="hours">9:00 to 5:00</div>
      <a class="book" href="#">GET AN APPOINTMENT</a>
    </section>
  </main>

  <footer class="site-footer">
    <small>©2013 Vexaro. All Rights Reserved.</small>
    <div class="social">
      <a href="#" aria-label="Social profile one"></a>
      <a href="#" aria-label="Social profile two"></a>
      <a href="#" aria-label="Social profile three"></a>
    </div>
  </footer>
</body>
</html>
```